Tovrin Mobile Phone colors and content

Looking to have an impact both on messaging and colors for my mobile website
www.quilvantohar.loan
also, i have upload my first draft of the mobile site, including messaging. that is open to the designer. In the end, i want the mobile phone messaging to resonate for someone who wants to build their credit.
Dont worry about the color combination on the document.

Target Market(s)

Finance - those with super poor credit.

Industry/Entity Type

Finance - credit building

Number of Pages Required

5+ page

Font styles to use
Other font styles liked:
• Inter

Requirements
Must have
• flow and impact
Nice to have
• look at the documents uploaded
Should not have
• not have dark background colors. background should be white.

```html
<!DOCTYPE html>
<html lang="en">
<head>
<meta charset="utf-8">
<title>Tovrin – Rebuild Credit in 3 Steps</title>
<link rel="stylesheet" href="https://fonts.googleapis.com/css2?family=Inter:wght@400;500;600&family=Rubik:wght@600;700&display=swap">
<style>
  :root{
    --stage:#062a4d;
    --screen:#ffffff;
    --ink:#101418;
    --muted:#6a6f75;
    --green:#12a84a;
    --green-soft:#eaf7ef;
    --button:#0b4f96;
  }
  *{box-sizing:border-box;margin:0;padding:0}
  html,body{width:1200px;height:516px;overflow:hidden}
  body{background:var(--stage);font-family:"Inter",sans-serif;position:relative}
  .screen{position:absolute;top:69px;width:175px;height:379px;background:var(--screen);border-radius:24px;overflow:hidden}
  .screen > *{position:absolute}
  .headline{font-family:"Rubik",sans-serif;font-weight:700;color:var(--ink);font-size:14px;line-height:15.5px;left:8px;right:8px;text-align:center}
  .headline--left{text-align:left;left:14px;right:8px}
  .accent{color:var(--green)}
  .body-copy{font-size:8.6px;line-height:13.5px;color:var(--muted);left:8px;right:8px;text-align:center}
  .body-copy p+p{margin-top:3.5px}
  .body-copy--left{text-align:left;left:14px;right:6px}
  .step-pill{left:50%;transform:translateX(-50%);height:14px;padding:0 7px;border-radius:7px;background:var(--green-soft);color:var(--green);font-size:7px;line-height:14px;white-space:nowrap}
  .apply-button{left:14px;right:14px;height:27px;border-radius:3px;background:var(--button);color:#fff;font-weight:600;font-size:9px;line-height:27px;text-align:center}
  .fine-print{left:0;right:0;text-align:center;font-size:7px;color:#444;font-weight:500}
  .mascot{left:50%;transform:translateX(-50%);width:90px;height:102px;border-radius:8px;background:linear-gradient(180deg,#f3d9b8,#cfe0f2 55%,#1f4e8c)}
  .mascot-name{left:0;right:0;text-align:center;font-size:11px;color:var(--ink);font-weight:500}
  .feature-list{left:14px;right:8px;list-style:none}
  .feature{display:flex;gap:8px;font-size:8.6px;line-height:13.5px;color:var(--muted)}
  .feature+.feature{margin-top:1px}
  .feature-icon{flex:none;width:19px;height:19px;border-radius:50%;background:#fff;box-shadow:0 1px 3px rgba(0,0,0,.15);display:flex;align-items:center;justify-content:center;margin-top:1px}
  .card-badge{left:50%;transform:translateX(-50%);width:28px;height:28px;border-radius:50%;background:#fff;box-shadow:0 2px 5px rgba(0,0,0,.15);display:flex;align-items:center;justify-content:center}
  .badge-dot{width:3px;height:3px;border-radius:50%;background:var(--green);left:98px;top:45px}
  .card-art{left:14px;right:14px;height:76px;border-radius:3px;background:linear-gradient(135deg,#1c4f92,#0b2f63 60%,#123a72)}
</style>
</head>
<body>

<section class="screen" style="left:103px">
  <h1 class="headline headline--left" style="top:70px;font-size:14.5px;line-height:17px">A Better Way to Rebuild Credit — <span class="accent">3 Bold Steps</span></h1>
  <div class="body-copy body-copy--left" style="top:127px">Rebuilding your credit? We’ll help you do it effectively—with real tools, real progress, and real incentives.</div>
  <div class="apply-button" style="top:293px">Apply Now</div>
  <div class="fine-print" style="top:326px">No impact on your credit score</div>
</section>

<section class="screen" style="left:308px">
  <div class="mascot" style="top:27px" role="img" aria-label="Illustrated credit coach mascot holding a credit score gauge"></div>
  <div class="mascot-name" style="top:134px">Keel Coach</div>
  <div class="step-pill" style="top:164px">Step 1</div>
  <h2 class="headline" style="top:183px;left:4px;right:4px">A $2,000 <span class="accent">Credit Builder Loan</span></h2>
  <ul class="feature-list" style="top:222px">
    <li class="feature"><span class="feature-icon"><svg width="9" height="10" viewBox="0 0 9 10" fill="none" stroke="#12a84a" stroke-width="1"><path d="M1 .5h4.5L8 3v6.5H1z"/><path d="M2.8 5h3.4M2.8 7h3.4"/></svg></span><span>Make on-time payments on a $2,000 Credit Builder Loan designed to help establish real credit history.</span></li>
    <li class="feature"><span class="feature-icon"><svg width="11" height="8" viewBox="0 0 11 8" fill="none" stroke="#12a84a" stroke-width="1"><rect x=".5" y=".5" width="10" height="7" rx="1"/><path d="M.5 3h10"/></svg></span><span>As you progress, you unlock a Vantacard credit card option.</span></li>
  </ul>
  <div class="apply-button" style="top:332px">Apply Now</div>
</section>

<section class="screen" style="left:513px">
  <div class="card-badge" style="top:46px"><svg width="15" height="11" viewBox="0 0 15 11" fill="none" stroke="#12a84a" stroke-width="1.3"><rect x=".7" y=".7" width="13.6" height="9.6" rx="1.5"/><path d="M.7 4h13.6"/></svg></div>
  <span class="badge-dot"></span>
  <div class="step-pill" style="top:84px">Step 2 – Platinum Rise Status</div>
  <h2 class="headline" style="top:102px">We <span class="accent">Put Our Money</span> Where Our Mouth Is</h2>
  <div class="body-copy" style="top:142px">
    <p>Upon reaching Platinum Rise Status, eligible members may receive a matching contribution of up to $150 toward an approved secured credit card.</p>
    <p>A strong on-time payment history with us is required.</p>
    <p>Your responsible progress unlocks real value—not gimmicks.</p>
  </div>
  <div class="apply-button" style="top:332px">Apply Now</div>
</section>

<section class="screen" style="left:718px">
  <div class="step-pill" style="top:43px">Step 3 – Elite Status</div>
  <h2 class="headline" style="top:63px">Graduate to a larger credit line with an <span class="accent">Unsecured Vantacard Creditcard</span></h2>
  <div class="card-art" style="top:140px" role="img" aria-label="Illustration of a blue unsecured credit card"></div>
  <div class="body-copy" style="top:229px">
    <p>Continued responsible use may qualify you for a higher-credit-limit unsecured credit card.</p>
    <p>No security deposit would be required.</p>
  </div>
  <div class="apply-button" style="top:332px">Apply Now</div>
</section>

<section class="screen" style="left:923px">
  <h2 class="headline" style="top:89px">Ongoing Credit <span class="accent">Wellness</span></h2>
  <div class="body-copy" style="top:133px">
    <p>Track your progress, monitor your credit, and get guidance along the way.</p>
    <p>Keel Coach helps you understand what matters—and provides concrete strategies to improve your credit.</p>
  </div>
  <div class="apply-button" style="top:332px">Apply Now</div>
</section>

</body>
</html>
```